Consulting firm needs elegant, modern designs

Business card design - I have a logo which has previously been developed for K-Pathways - I will attach. I will also attach specifications for the size of the business card.

We also need a logo design for our leadership consulting product - Frame of Guidance - we focus on improving workplace health by educating leaders and learning professionals about how the physical and emotional affects performance and engagement. I have some example logos and ideas which I will attach - these have attempted to bring in the body but I do not like the font (see www.frameofguidance.example for preferred font). Idea is to please have a 'body' visible somehow in the word Leadership, ensuring that this conveys flexibility and agility. Colors which I prefer are deep purple OR turquoise, together with silver. COLORS below are for LOGO design.

Target Market(s)

For the business card, it should be more masculine. The logo which will be attached should be neutralized into dark blue shades and silver. The business card K-Pathways is focused on business transformation - organizations who would require a consultant to help them enter new markets, for example.

Industry/Entity Type

Leadership

Contact Information for Business Card

Content:
K-Pathways
Molenkade 27
4921KT, Breda, The Netherlands
maarten@K-Pathways.example
www.K-Pathways.example

Colors for business card should be conservative and slightly more masculine. Use the K-Pathways logo but change the colors to blue or shades of gray/black.

Dimensions for cut
85 x 55 mm
1004 x 650 pixels
Full document size
88 x 58 mm
1040 x 685 pixels
For the best result, you need to design the full document size including the bleed

Logo Text

Frame of Guidance

Font styles to use
Serif
Sans Serif

Colors
876aae
333333
959595

Requirements
Must have
• Professional, modern and unique business card design
• Professional, elegant, and modern logo design - with creative thinking
Should not have
• Too many colors

```html
<!DOCTYPE html>
<html lang="en">
<head>
<meta charset="utf-8">
<title>K-Pathways Business Card</title>
<link rel="stylesheet" href="https://fonts.googleapis.com/css2?family=Montserrat:wght@600&family=Open+Sans:wght@400;600&display=swap">
<style>
  :root {
    --purple: #876aae;
    --purple-deep: #5e4592;
    --charcoal: #333333;
    --silver: #959595;
    --silver-light: #d6d6d6;
    --lavender: #c9bddc;
    --mint: #cfe9e6;
    --ink: #1e1b3a;
    --paper: #ffffff;
    --backdrop: #e4e4e6;
  }
  html, body {
    margin: 0;
    width: 1200px;
    height: 1200px;
    overflow: hidden;
    background: var(--backdrop);
  }
  .sheet {
    position: relative;
    width: 1200px;
    height: 1200px;
  }
  .card {
    position: absolute;
    left: 182px;
    width: 835px;
    height: 540px;
    box-shadow: 0 6px 18px rgba(0,0,0,0.18);
  }
  .card--back { top: 40px; }
  .card--front { top: 620px; }
  .card svg { display: block; }
  .brand-name { font-family: 'Montserrat', sans-serif; font-weight: 600; }
  .contact { font-family: 'Open Sans', sans-serif; }
</style>
</head>
<body>
<main class="sheet">

  <!-- Back side -->
  <section class="card card--back" aria-label="Business card back">
    <svg width="835" height="540" viewBox="0 0 835 540">
      <defs>
        <linearGradient id="silver-arc" x1="0" y1="0" x2="1" y2="1">
          <stop offset="0" stop-color="#f4f4f4"/>
          <stop offset="0.5" stop-color="#959595"/>
          <stop offset="1" stop-color="#e8e8e8"/>
        </linearGradient>
        <radialGradient id="mark-glow" cx="0.5" cy="0.5" r="0.5">
          <stop offset="0" stop-color="#4a3f6a"/>
          <stop offset="1" stop-color="#3a4a55" stop-opacity="0.6"/>
        </radialGradient>
        <clipPath id="back-clip"><rect width="835" height="540"/></clipPath>
      </defs>
      <g clip-path="url(#back-clip)">
        <rect class="back-field" width="835" height="540" fill="var(--purple)"/>
        <circle class="back-disc" cx="250" cy="330" r="470" fill="var(--charcoal)"/>
        <path class="back-arc" d="M 340 -130 A 470 470 0 0 1 700 250" fill="none" stroke="url(#silver-arc)" stroke-width="7"/>
        <ellipse class="back-decoration" role="img" aria-label="Faint brand decoration" cx="140" cy="330" rx="260" ry="230" fill="url(#mark-glow)" opacity="0.7"/>
      </g>
      <circle class="brand-dot" cx="318" cy="262" r="34" fill="var(--paper)"/>
      <text class="brand-name" x="368" y="282" font-size="56" fill="var(--paper)">K-Pathways</text>
      <line x1="290" y1="420" x2="835" y2="420" stroke="var(--paper)" stroke-width="1.2" opacity="0.8"/>
      <text class="contact" x="300" y="470" font-size="17" fill="var(--paper)">www.K-Pathways.example</text>
    </svg>
  </section>

  <!-- Front side -->
  <section class="card card--front" aria-label="Business card front">
    <svg width="835" height="540" viewBox="0 0 835 540">
      <defs>
        <linearGradient id="deco-soft" x1="0" y1="0" x2="1" y2="1">
          <stop offset="0" stop-color="#c9bddc"/>
          <stop offset="0.6" stop-color="#b5a8d4"/>
          <stop offset="1" stop-color="#cfe9e6"/>
        </linearGradient>
        <clipPath id="front-clip"><rect width="835" height="540"/></clipPath>
      </defs>
      <g clip-path="url(#front-clip)">
        <rect width="835" height="540" fill="var(--paper)"/>
        <path class="top-strip" d="M0 18 H335 a12 12 0 0 1 0 24 H0 Z" fill="var(--purple)"/>
        <rect class="decoration" role="img" aria-label="Soft brand decoration in lavender and mint" x="600" y="0" width="235" height="330" fill="url(#deco-soft)" opacity="0.85"/>
        <path class="corner-band" d="M700 0 H835 V200 Z" fill="var(--purple-deep)" opacity="0.85"/>
        <rect class="tag-purple" x="420" y="0" width="110" height="165" fill="var(--purple)"/>
        <rect class="tag-dark" x="530" y="0" width="110" height="105" fill="var(--charcoal)"/>
        <text class="contact tag-label" x="452" y="90" font-size="24" fill="var(--paper)">K-Pathways</text>
        <path class="base-purple" d="M540 540 V440 a40 40 0 0 1 40 -40 H835 V540 Z" fill="var(--purple-deep)"/>
        <path class="base-dark" d="M0 540 V460 H520 a40 40 0 0 1 40 40 V540 Z" fill="var(--charcoal)"/>
      </g>

      <circle class="brand-dot" cx="66" cy="148" r="28" fill="var(--purple)"/>
      <text class="brand-name" x="106" y="164" font-size="44" fill="var(--ink)">K-Pathways</text>
      <line x1="0" y1="222" x2="520" y2="222" stroke="var(--charcoal)" stroke-width="1.2"/>

      <line x1="530" y1="235" x2="530" y2="295" stroke="var(--charcoal)" stroke-width="1.2"/>
      <text class="contact" x="545" y="258" font-size="19" font-weight="600" fill="var(--ink)">+31 65 218 3904</text>
      <text class="contact" x="545" y="286" font-size="17" fill="var(--ink)">maarten@K-Pathways.example</text>
      <text class="contact" x="575" y="370" font-size="18" fill="var(--ink)">www.K-Pathways.example</text>
      <line x1="575" y1="386" x2="835" y2="386" stroke="var(--charcoal)" stroke-width="1.2"/>

      <text class="contact" x="40" y="322" font-size="22" fill="var(--ink)">Address:</text>
      <line x1="40" y1="334" x2="270" y2="334" stroke="var(--charcoal)" stroke-width="1"/>
      <text class="contact" x="40" y="360" font-size="19" fill="var(--ink)">Molenkade 27</text>
      <text class="contact" x="40" y="386" font-size="19" fill="var(--ink)">4921KT, Breda, The Netherlands</text>
    </svg>
  </section>

</main>
</body>
</html>
```